Brindova Electrical Solutions needs a website

We need a new website designed because our current one is outdated. I would like a one-page website. We are a B2B company and want to maintain a professional appearance to appeal to project managers and directors.

for some reference, these are a few of my competitor's websites; we offer the same services.

https://valtrawire.com.au/services
https://www.drumwell.com.au/mechanical-electrical-services/
https://www.qulan.com.au/

Industry/Entity Type

Electrical

Number of Pages Required

1 page

Font styles to use
Sans Serif

Colors
0054AA
0677BA
7BADD7
CADEEF
E8F1F8

```html
<!DOCTYPE html>
<html lang="en">
<head>
<meta charset="utf-8">
<title>Brindova Electrical Solutions</title>
<link href="https://fonts.googleapis.com/css2?family=Montserrat:wght@400;500;600;700;800&display=swap" rel="stylesheet">
<style>
:root{
  --blue-deep:#0054AA;
  --blue:#0677BA;
  --blue-mid:#7BADD7;
  --blue-light:#CADEEF;
  --blue-pale:#E8F1F8;
  --ink:#000;
  --navy:#0b2a55;
  --card:#b3b3b3;
  --card-soft:#c9c9c9;
  --white:#fff;
  --text:#222;
}
*{box-sizing:border-box;margin:0;padding:0}
html,body{width:1200px;height:3028px;overflow:hidden;background:var(--white)}
body{position:relative;font-family:"Montserrat",Arial,sans-serif;color:var(--text)}
.abs{position:absolute}
.shapes{position:absolute;left:0;top:0;width:1200px;height:3028px}
/* header */
.site-header{position:absolute;left:0;top:0;width:1200px;height:88px;background:var(--ink);display:flex;align-items:center}
.brand{position:absolute;left:160px;font-size:26px;font-weight:800;color:var(--blue)}
.nav{position:absolute;left:390px;display:flex;gap:58px}
.nav a{color:var(--white);text-decoration:none;font-size:15px;font-weight:700;letter-spacing:.5px}
/* hero */
.hero-photo{left:160px;top:88px;width:900px;height:612px;background:linear-gradient(120deg,#6a7f92 0%,#2d3f58 35%,#1a2846 65%,#0f1a33 100%)}
.hero-copy{left:600px;top:370px;width:430px;color:var(--white);text-align:right}
.hero-copy h1{font-size:34px;line-height:1.2;font-weight:700}
.hero-copy p{margin-top:16px;font-size:12px;line-height:1.5;color:#dfe6f0}
/* services */
.services-title{left:0;top:775px;width:1200px;text-align:center;font-size:34px;font-weight:700;color:var(--ink)}
.services-grid{left:160px;top:870px;width:900px;display:grid;grid-template-columns:repeat(3,280px);column-gap:30px;row-gap:22px}
.service-card{background:var(--card);height:210px;padding:22px 18px}
.service-card.is-active{background:var(--card-soft);border:4px solid var(--ink)}
.service-card h3{font-size:19px;font-weight:700;color:var(--blue-deep);line-height:1.2;margin-bottom:12px}
.service-card p{font-size:11px;line-height:1.45;color:var(--white)}
/* about */
.about-band{left:0;top:1380px;width:1200px;height:540px;background:linear-gradient(180deg,#2c2c2c 0%,#1a1a1a 50%,#121212 100%)}
.about-copy{left:220px;top:1545px;width:760px;text-align:center;color:var(--white)}
.about-copy h2{font-size:38px;font-weight:700;margin-bottom:22px}
.about-copy p{font-size:13px;line-height:1.45}
/* why */
.why-photo{left:160px;top:2000px;width:352px;height:262px;border:4px solid var(--ink);background:linear-gradient(135deg,#d9dde2 0%,#8d96a3 45%,#3b4656 100%)}
.why-copy{left:672px;top:2030px;width:330px}
.why-copy h2{font-size:25px;font-weight:700;color:var(--navy);margin-bottom:24px}
.why-copy p{font-size:12px;line-height:1.5;color:var(--text)}
/* footer */
.footer-card{left:140px;top:2508px;width:920px;height:412px;background:var(--white);padding:0 28px}
.footer-col{position:absolute;top:0}
.footer-col h4{font-size:17px;font-weight:700;color:var(--ink);margin-top:0}
.col-social{left:28px;top:110px}
.social-list{margin-top:24px;display:flex;flex-direction:column;gap:24px}
.social-dot{width:20px;height:20px;border-radius:5px;background:var(--ink)}
.col-contact{left:262px;top:110px}
.contact-list{margin-top:24px;list-style:none;display:flex;flex-direction:column;gap:22px}
.contact-list li{display:flex;align-items:center;gap:14px;font-size:11px;line-height:1.3}
.contact-list svg{width:20px;height:20px;flex:none}
.col-company{left:562px;top:116px;width:330px}
.col-company p{margin-top:40px;font-size:11px;line-height:1.5}
.btn-more{display:inline-block;margin-top:24px;background:var(--ink);color:var(--white);font-size:13px;font-weight:700;padding:12px 22px;border-radius:8px;letter-spacing:.5px}
</style>
</head>
<body>
<svg class="shapes" viewBox="0 0 1200 3028" aria-hidden="true">
  <polygon points="0,650 560,650 560,700 0,920" fill="#000"/>
  <polygon points="1200,1920 1200,2330 920,1920" fill="#000"/>
  <polygon points="0,2470 1200,2360 1200,3028 0,3028" fill="#000"/>
  <polygon points="0,2900 520,3028 0,3028" fill="#fff"/>
</svg>

<header class="site-header">
  <div class="brand">Brindova</div>
  <nav class="nav">
    <a href="#">HOME</a><a href="#">SERVICES</a><a href="#">ABOUT US</a><a href="#">CONTACT US</a>
  </nav>
</header>

<div class="abs hero-photo" role="img" aria-label="Electrician in hard hat and safety glasses working on a wired switchboard"></div>
<section class="abs hero-copy">
  <h1>Simplifying Mechanical and Electrical Services for B2B Success</h1>
  <p>Reliable commercial electrical and mechanical services built for project managers and directors, with safe work, clear reporting and fast response on every site, every time.</p>
</section>

<h2 class="abs services-title">Services that we offer</h2>
<section class="abs services-grid">
  <article class="service-card"><h3>24-Hour emergency breakdown repairs</h3><p>When equipment fails, our technicians respond day or night to restore power quickly and keep your operations running with minimal downtime.</p></article>
  <article class="service-card"><h3>Routine electrical maintenance</h3><p>Scheduled inspections and servicing that find faults early, extend asset life and keep your sites compliant and safe throughout the year.</p></article>
  <article class="service-card is-active"><h3>RCD testing</h3><p>Regular residual current device testing to confirm fast tripping, protect your staff and meet workplace safety standards.</p></article>
  <article class="service-card"><h3>Emergency light testing</h3><p>Full testing of exit and emergency lighting with clear reports, so your building stays compliant and safe in an outage.</p></article>
  <article class="service-card"><h3>Test &amp; Tag</h3><p>Portable appliance testing and tagging across your sites, with accurate records and quick turnaround to suit your schedule.</p></article>
  <article class="service-card"><h3>Thermal imaging – infrared thermographic scanning</h3><p>Infrared scans that reveal hot spots and loose connections before they cause failures or fires.</p></article>
</section>

<div class="abs about-band" role="img" aria-label="Dark photo of engineers reviewing plans in an office"></div>
<section class="abs about-copy">
  <h2>About Us</h2>
  <p>At Brindova Electrical Solutions we specialise in delivering high quality mechanical and electrical services tailored for businesses. As a trusted B2B partner, we focus on providing reliable solutions that meet the unique needs of project managers, directors, and industry leaders.</p>
  <p>With years of experience, our team is dedicated to precision, efficiency, and excellence in every project we undertake. Whether it's electrical installations, mechanical upgrades, or ongoing maintenance, we are committed to ensuring your projects run smoothly and efficiently.</p>
  <p>Our professional approach and customer first philosophy make us the go to partner for businesses seeking expertise and reliability. Let us power your success with solutions you can trust.</p>
</section>

<div class="abs why-photo" role="img" aria-label="Business partners shaking hands over a signed contract"></div>
<section class="abs why-copy">
  <h2>Why Choose Us?</h2>
  <p>At Brindova Electrical Solutions we pride ourselves on delivering professional, reliable, and tailored mechanical and electrical solutions designed specifically for businesses. With a strong focus on meeting the needs of project managers and directors, we provide customised services that ensure efficiency and precision in every project. Our B2B expertise, combined with a commitment to sustainability and innovation, allows us to offer smarter, eco friendly solutions that align with modern industry standards. Backed by a proven track record of successful projects and a team of skilled professionals, we are dedicated to supporting your projects with exceptional quality and service every step of the way.</p>
</section>

<footer class="abs footer-card">
  <div class="footer-col col-social">
    <h4>Social Links</h4>
    <div class="social-list">
      <span class="social-dot"></span><span class="social-dot"></span><span class="social-dot"></span><span class="social-dot"></span>
    </div>
  </div>
  <div class="footer-col col-contact">
    <h4>Contact Information</h4>
    <ul class="contact-list">
      <li><svg viewBox="0 0 24 24"><path d="M12 2a7 7 0 0 0-7 7c0 5 7 13 7 13s7-8 7-13a7 7 0 0 0-7-7zm0 9.5A2.5 2.5 0 1 1 12 6.5a2.5 2.5 0 0 1 0 5z" fill="#000"/></svg><span>2150 Alder Lane<br>Suite 12</span></li>
      <li><svg viewBox="0 0 24 24"><circle cx="12" cy="12" r="10" fill="none" stroke="#000" stroke-width="2"/><path d="M2 12h20M12 2c3 3 3 17 0 20M12 2c-3 3-3 17 0 20" fill="none" stroke="#000" stroke-width="1.5"/></svg><span>info@brindova.com</span></li>
      <li><svg viewBox="0 0 24 24"><rect x="3" y="5" width="18" height="14" rx="2" fill="none" stroke="#000" stroke-width="2"/><path d="M3 6l9 7 9-7" fill="none" stroke="#000" stroke-width="2"/></svg><span>info@brindova.com</span></li>
      <li><svg viewBox="0 0 24 24"><path d="M6.6 10.8a15 15 0 0 0 6.6 6.6l2.2-2.2a1 1 0 0 1 1-.25 11.4 11.4 0 0 0 3.6.6 1 1 0 0 1 1 1V20a1 1 0 0 1-1 1A17 17 0 0 1 3 4a1 1 0 0 1 1-1h3.5a1 1 0 0 1 1 1c0 1.25.2 2.450.6 3.6a1 1 0 0 1-.25 1z" fill="#000"/></svg><span>555-014-2290</span></li>
    </ul>
  </div>
  <div class="footer-col col-company">
    <h4>Company</h4>
    <p>Trusted commercial electrical and mechanical partner. Safe work, clear reports and fast response for every business we serve, across every site.</p>
    <span class="btn-more">LEARN MORE</span>
  </div>
</footer>
</body>
</html>
```